NEW Gym Timetable for Muay Thai gym!

We need a new timetable for our Muay Thai gym - the times, classes and logos are attached. Our primary logo font is MACHINE BT

The gym is called Kalto Vex. The address is Level 2, 218-220 Brannock Road, Pellwood, Canberra

We are open Monday to Saturday and Sunday by appointment.

Our website and more information can be found at www.kaltovex.com.au.

Please message me for more information/feedback

```html
<!DOCTYPE html>
<html lang="en">
<head>
<meta charset="utf-8">
<title>Kalto Vex Timetable</title>
<link href="https://fonts.googleapis.com/css2?family=Anton&family=Open+Sans:wght@400;600;700;800&display=swap" rel="stylesheet">
<style>
:root{
  --green:#0b8a44;
  --green-dark:#06672f;
  --ink:#12181d;
  --panel:#1a232a;
  --cell:#eeeeee;
  --cell-alt:#e2e2e2;
  --text:#333;
  --silver:#c9cccf;
  --page:#ececec;
}
*{box-sizing:border-box;margin:0;padding:0}
html,body{width:830px;height:1200px;overflow:hidden;background:var(--page)}
body{font-family:"Open Sans",sans-serif;position:relative}
.timetable{
  position:absolute;left:20px;top:320px;width:790px;height:560px;overflow:hidden;
  background:radial-gradient(ellipse at 50% 30%,#26313a 0%,var(--panel) 45%,var(--ink) 100%);
  box-shadow:0 6px 18px rgba(0,0,0,.3);
}
.badge{position:absolute;left:22px;top:0;width:143px;height:139px}
.badge-name{
  position:absolute;left:22px;top:52px;width:143px;text-align:center;
  font-family:"Open Sans",sans-serif;font-weight:800;font-size:19px;color:var(--green);
}
.headline{
  position:absolute;left:196px;top:14px;width:400px;text-align:center;
  font-family:"Anton",sans-serif;font-size:66px;line-height:72px;color:var(--green);letter-spacing:1px;
}
.subline{
  position:absolute;left:196px;width:400px;text-align:center;
  font-family:"Anton",sans-serif;color:var(--silver);font-size:25px;line-height:30px;letter-spacing:.5px;
}
.subline.days{top:90px}
.subline.appt{top:123px}
.schedule{
  position:absolute;left:20px;top:164px;width:749px;height:235px;
  display:grid;grid-template-columns:repeat(7,1fr);grid-template-rows:37px 57px 47px 47px 47px;
  background:var(--cell);
}
.day{
  background:linear-gradient(#0e9a4c,var(--green-dark));color:#fff;font-weight:700;font-size:15px;
  display:flex;align-items:center;justify-content:center;border-right:1px solid #0a7a3c;
}
.slot{
  display:flex;flex-direction:column;align-items:center;justify-content:center;text-align:center;
  border-right:1px solid #cfcfcf;border-bottom:1px solid #d6d6d6;
  background:linear-gradient(#f4f4f4,var(--cell-alt));font-size:8.5px;color:var(--text);line-height:14px;
}
.slot .time{color:var(--green);font-weight:700;font-size:9.5px}
.slot.span{grid-row:span 2}
.slot.empty{background:linear-gradient(#f0f0f0,var(--cell-alt))}
.contact-bar{
  position:absolute;left:128px;top:412px;width:533px;height:24px;border-radius:5px;
  background:linear-gradient(#0e9a4c,var(--green-dark));color:#fff;
  display:flex;align-items:center;justify-content:center;gap:9px;font-size:11px;font-weight:600;
}
.contact-bar .divider{width:1px;height:13px;background:#fff;opacity:.7}
.contact-bar .web{font-weight:400;font-size:12px}
.social{position:absolute;left:355px;top:449px;width:80px;height:26px}
.gear-photo{
  position:absolute;left:0;bottom:0;width:790px;height:110px;
  background:linear-gradient(180deg,rgba(20,28,34,0) 0%,#2b3a45 55%,#cfd6db 100%);
}
</style>
</head>
<body>
<main class="timetable">
  <svg class="badge" viewBox="0 0 143 139" aria-hidden="true">
    <path d="M0 0H143V105L71.5 139L0 105Z" fill="#b9bec2"/>
    <path d="M4 0H139V102L71.5 134L4 102Z" fill="#f3f3f3"/>
  </svg>
  <div class="badge-name">Kalto Vex</div>

  <h1 class="headline">WE ARE OPEN</h1>
  <p class="subline days">MONDAY TO SATURDAY AND SUNDAY</p>
  <p class="subline appt">BY APPOINTMENT</p>

  <section class="schedule">
    <div class="day">Monday</div><div class="day">Tuesday</div><div class="day">Wednesday</div><div class="day">Thursday</div><div class="day">Friday</div><div class="day">Saturday</div><div class="day">Sunday</div>

    <div class="slot"><span class="time">6.00AM — 7:00AM</span>Clinching<br>(Fighters/By invitation)</div>
    <div class="slot"><span class="time">6:00AM—6:45AM</span>Muay HiiT</div>
    <div class="slot"><span class="time">6.00AM — 7:00AM</span>Clinching<br>(Fighters/By invitation)</div>
    <div class="slot"><span class="time">6:00AM—6:45AM</span>Muay HiiT</div>
    <div class="slot empty"></div>
    <div class="slot"><span class="time">8.00AM —8:45AM</span>Muay HiiT<br>(Fighters/By invitation)</div>
    <div class="slot empty"></div>

    <div class="slot"><span class="time">5:30PM — 6:30PM</span>Muay Thai</div>
    <div class="slot"><span class="time">5:30PM— 6:30PM</span>Boxing</div>
    <div class="slot"><span class="time">5:30PM — 6:30PM</span>Muay Thai</div>
    <div class="slot"><span class="time">5:30PM— 6:30PM</span>Boxing</div>
    <div class="slot"><span class="time">5:30PM —7:00 PM</span>Muay Thai Weekly wrap</div>
    <div class="slot"><span class="time">9:00AM—11:00AM</span>Sparring</div>
    <div class="slot"><span style="font-size:10px">Personal Training<br>By Appointment</span></div>

    <div class="slot"><span class="time">6:30PM — 7:30PM</span>Padwork &amp; Bagwork</div>
    <div class="slot"><span class="time">6:30PM — 7:30PM</span>Muay Thai</div>
    <div class="slot"><span class="time">6:30PM — 7:30PM</span>Padwork &amp; Bagwork</div>
    <div class="slot"><span class="time">6:30PM — 7:30PM</span>Muay Thai</div>
    <div class="slot empty"></div>
    <div class="slot"><span class="time">12:00PM — 1:00PM</span>Muay Thai</div>
    <div class="slot empty"></div>

    <div class="slot"><span class="time">7:30 PM — 8:30 PM</span>Fighters</div>
    <div class="slot"><span class="time">6:30 PM — 8:30 PM</span>Fighters</div>
    <div class="slot"><span class="time">7:30 PM — 8:30 PM</span>Fighters</div>
    <div class="slot"><span class="time">6:30 PM — 8:30 PM</span>Fighters</div>
    <div class="slot empty"></div>
    <div class="slot empty"></div>
    <div class="slot empty"></div>
  </section>

  <div class="gear-photo" role="img" aria-label="Photo of a row of dumbbells in increasing size on a dark floor"></div>

  <div class="contact-bar">
    <svg width="11" height="11" viewBox="0 0 12 12" aria-hidden="true"><circle cx="6" cy="6" r="5.3" fill="none" stroke="#fff"/><path d="M6 2.6a2.2 2.2 0 0 1 2.2 2.2C8.2 6.5 6 9 6 9S3.8 6.5 3.8 4.8A2.2 2.2 0 0 1 6 2.6Z" fill="#fff"/></svg>
    <span>Level 2, 218-220 Brannock Road, Pellwood, Canberra</span>
    <span class="divider"></span>
    <svg width="11" height="11" viewBox="0 0 12 12" aria-hidden="true"><circle cx="6" cy="6" r="5.3" fill="none" stroke="#fff"/><circle cx="6" cy="6" r="2.6" fill="#fff"/></svg>
    <span class="web">www.kaltovex.com.au</span>
  </div>

  <svg class="social" viewBox="0 0 80 26" aria-label="Social media links">
    <g fill="none" stroke="#fff" stroke-width="1.5">
      <circle cx="13" cy="13" r="11.5"/><circle cx="40" cy="13" r="11.5"/><circle cx="67" cy="13" r="11.5"/>
    </g>
  </svg>
</main>
</body>
</html>
```